The Lindenmoor Compass Book

Cover Design for my first book. The book is for elementary school principals who are unhappy and are considering a career change but are afraid to leave. I teach them how to develop emotional fitness and resiliency through thought management so that they can decide whether to stay or leave their position from a place of empowerment. I've attached my podcast artwork for your reference. My publisher suggested not having me on the cover which is fine. I just thought it might be helpful.

Target Market(s)

Elementary School Principals

Industry/Entity Type

Education

Logo Text

The Lindenmoor Compass

Font styles to use
Serif
Sans Serif

Colors
34a6d7
33b8a4
3276b5

Requirements
Must have
• Title, Author name, photo or artwork that captures the essence of the book

```html
<!DOCTYPE html>
<html lang="en">
<head>
<meta charset="utf-8">
<title>The Lindenmoor Compass – Book Cover</title>
<link rel="stylesheet" href="https://fonts.googleapis.com/css2?family=Oswald:wght@600;700&family=Montserrat:wght@500;800&display=swap">
<style>
  :root {
    --stage: #d9dbdd;
    --glow: #f4f1c9;
    --sun-gold: #d9c235;
    --sky-teal: #33b8a4;
    --sky-blue: #34a6d7;
    --deep-blue: #3276b5;
    --night: #0b1c2a;
    --ink-black: #060d14;
    --title-yellow: #f3e61b;
    --author-white: #ffffff;
  }
  * { margin: 0; padding: 0; box-sizing: border-box; }
  html, body {
    width: 1200px;
    height: 900px;
    overflow: hidden;
    background: radial-gradient(ellipse at 50% 45%, #eceef0 0%, var(--stage) 70%, #c9cbce 100%);
  }
  .cover {
    position: absolute;
    left: 160px;
    top: 150px;
    width: 880px;
    height: 600px;
    overflow: hidden;
    background: var(--night);
  }
  .cover-artwork {
    position: absolute;
    inset: 0;
    background:
      radial-gradient(ellipse 38% 45% at 30% 22%, var(--glow) 0%, rgba(244,241,201,0.55) 40%, rgba(244,241,201,0) 100%),
      radial-gradient(ellipse 20% 24% at 16% 58%, rgba(52,166,215,0.9) 0%, rgba(51,184,164,0.6) 55%, rgba(51,184,164,0) 100%),
      radial-gradient(ellipse 30% 40% at 48% 62%, rgba(200,214,220,0.55) 0%, rgba(200,214,220,0) 100%),
      radial-gradient(ellipse 26% 60% at 80% 45%, rgba(6,13,20,0.95) 0%, rgba(6,13,20,0.6) 60%, rgba(6,13,20,0) 100%),
      linear-gradient(115deg, var(--sun-gold) 0%, #a9c25a 18%, var(--sky-teal) 38%, var(--deep-blue) 58%, var(--night) 78%, var(--ink-black) 100%);
  }
  .facets {
    position: absolute;
    inset: 0;
    width: 100%;
    height: 100%;
  }
  .title-block {
    position: absolute;
    right: 70px;
    top: 190px;
    text-align: left;
  }
  .title {
    font-family: "Oswald", "Arial Narrow", sans-serif;
    font-weight: 700;
    color: var(--title-yellow);
    text-transform: uppercase;
    line-height: 0.92;
    letter-spacing: 1px;
  }
  .title-the { display: block; font-size: 56px; }
  .title-main { display: block; font-size: 78px; }
  .author {
    margin-top: 18px;
    font-family: "Montserrat", "Helvetica Neue", sans-serif;
    color: var(--author-white);
    text-transform: uppercase;
    font-size: 17px;
    letter-spacing: 2px;
  }
  .author-with { font-weight: 500; margin-right: 6px; }
  .author-name { font-weight: 800; }
</style>
</head>
<body>
  <div class="cover">
    <div class="cover-artwork" role="img" aria-label="Cover photograph: a woman in a dark jacket holding the Earth in her outstretched hand against sunlit clouds and light rays"></div>
    <svg class="facets" viewBox="0 0 880 600" preserveAspectRatio="none" aria-hidden="true">
      <polygon points="0,0 260,0 120,180" fill="#ffffff" opacity="0.06"/>
      <polygon points="420,0 620,0 540,220" fill="#ffffff" opacity="0.05"/>
      <polygon points="560,600 880,380 880,600" fill="#000000" opacity="0.18"/>
      <polygon points="0,600 0,420 200,600" fill="#ffffff" opacity="0.06"/>
    </svg>
    <div class="title-block">
      <h1 class="title">
        <span class="title-the">The</span>
        <span class="title-main">Lindenmoor</span>
        <span class="title-main">Compass</span>
      </h1>
      <p class="author"><span class="author-with">With</span><span class="author-name">Marisol Dane Whitcombe</span></p>
    </div>
  </div>
</body>
</html>
```